Stationery Design and Business Card

Incorporate recently designed new logo onto updated letterhead, with compliments slips, email footer and business cards. Must include all other professional branding that is on existing stationery. The letterhead is over 10 years old so would like it made more contemporary. Perhaps a little cleaner.
One professional brand has changed slightly. New file attached.

Target Market(s)

Clients of accounting firm Other professionals.

Industry/Entity Type

Accounting

Contact Information for Business Card

Existing business card included in stationery file upload. New logo has now been uploaded to the files provided

Requirements
Must have
• Existing professional body branding. There are color restrictions on how the branding can be used. Information about the Super Fund Expert logo is included in uploaded files. As color is restricted on this branding the other elements of the stationery must fit with that.
Nice to have
• Prefer not to have too many colors that would add a lot of additional costs when having stationery printed.

```html
<!DOCTYPE html>
<html lang="en">
<head>
<meta charset="utf-8">
<title>Business Card</title>
<link rel="stylesheet" href="https://fonts.googleapis.com/css2?family=Cabin:wght@400&display=swap">
<style>
  :root {
    --paper: #ffffff;
    --ink: #111111;
    --brand-blue: #1a7aff;
    --pattern-light: #eaf2fd;
    --pattern-mid: #cfe0f8;
    --pattern-sky: #d4ecfb;
  }
  html, body {
    margin: 0;
    padding: 0;
    overflow: hidden;
    background: var(--paper);
  }
  .card {
    position: relative;
    width: 1200px;
    height: 720px;
    background: var(--paper);
    overflow: hidden;
    font-family: "Cabin", "Trebuchet MS", sans-serif;
    color: var(--ink);
  }
  .pattern-field {
    position: absolute;
    inset: 0;
    width: 1200px;
    height: 720px;
  }
  .badge {
    position: absolute;
    left: 78px;
    top: 96px;
    width: 260px;
    display: flex;
    flex-direction: column;
    align-items: center;
    gap: 18px;
  }
  .badge-square {
    width: 150px;
    height: 150px;
    background: var(--brand-blue);
  }
  .badge-name {
    font-size: 27px;
    line-height: 1.1;
    color: var(--brand-blue);
    text-align: center;
    letter-spacing: 0.04em;
    text-transform: uppercase;
  }
  .contact {
    position: absolute;
    left: 362px;
    top: 146px;
  }
  .contact p { margin: 0; }
  .person-name {
    font-size: 44px;
    line-height: 56px;
  }
  .person-title {
    font-size: 27px;
    line-height: 30px;
    margin-bottom: 12px !important;
  }
  .contact-line {
    font-size: 35px;
    line-height: 52px;
  }
  .address {
    margin-top: 10px !important;
    font-size: 35px;
    line-height: 41px;
  }
</style>
</head>
<body>
  <main class="card">
    <svg class="pattern-field" viewBox="0 0 1200 720" role="img" aria-label="Scattered light blue outlined hexagon pattern along the right edge and bottom of the card">
      <defs>
        <linearGradient id="pattern-tone" x1="0" y1="0" x2="0.6" y2="1">
          <stop offset="0" stop-color="var(--pattern-sky)"/>
          <stop offset="0.5" stop-color="var(--pattern-light)"/>
          <stop offset="1" stop-color="var(--pattern-mid)"/>
        </linearGradient>
      </defs>
      <path d="M1080 0 H1200 V720 H0 V600 C120 560 320 530 480 520 C640 505 800 470 900 420 C980 380 1020 300 1040 200 C1055 120 1060 50 1080 0 Z" fill="url(#pattern-tone)" opacity="0.75"/>
    </svg>

    <div class="badge">
      <div class="badge-square"></div>
      <div class="badge-name">Super Fund Expert</div>
    </div>

    <section class="contact">
      <p class="person-name">First Name Last Name</p>
      <p class="person-title">Title</p>
      <p class="contact-line">Phone: 111-111-1111</p>
      <p class="contact-line">Email: first.last@example.com</p>
      <p class="address">PO Box 4410 / 17 Harbour Lane<br>Marlow Bay WA 6999<br>ABN 98 765 432 100</p>
    </section>
  </main>
</body>
</html>
```